Resinex Pro color chart design

We are in need to have a color chart (pdf to be displayed on our website-www.resinexpro-sample.com as well as for print) to show customers what their color choices are for our metallic epoxy pigments. We would like it to be modern amd clean. A white background will allow the color swatches to stand out. our company colors are orange, grey and white. Looking for the color swatches to be as large as possible while still being able to display our logo, contact info and disclaimers. We are open to any design ideas. If needed it can be put on two pages.

Additional info to add: Resinex Pro Shimmer Tint Powders are special effect pigments composed of mica nano-particles coated with various organic and inorganic pigments to create pearlescent and iridescent effects that mimic the
natural look of stone and rock formations. These unique pigments are designed to be field blended with Resinex Pro Artisan Lustre clear epoxy. When the metallic particles are mixed with our epoxy they give the coating a shine that reflects light and creates an eye-catching dramatic color. For the most vivid color and dynamic effects we recommend (1) 16oz jar of metallic pigment for each 3 Gallon kit of our Artisan Lustre Epoxy.

Disclaimer: The colors on this chart are represented as closely as possible. Variations should be expected due to differences in substrate conditions, thickness of application, speed of curing, blending of colors, application technique, color of initial primer coat and screen resolution. For additional information and application instructions visit www.resinexpro-sample.com

Contact info: Tel. 1-800-555-0147
www.resinexpro-sample.com

Target Market(s)

Online. This will be a link on our website

Font styles to use
Sans Serif

Colors
f37122
5c5c5c
ffffff

Requirements
Must have
• A white background will allow the color swatches to stand out. Disclaimer should be in small print but still readable.
Nice to have
• Can use our company colors as part of the design
Should not have
• Should not look and feel cluttered.

```html
<!DOCTYPE html>
<html lang="en">
<head>
<meta charset="utf-8">
<title>Resinex Pro – Shimmer Tint Powders Colour Chart</title>
<link rel="stylesheet" href="https://fonts.googleapis.com/css2?family=Open+Sans:wght@400;600;700&family=Roboto+Condensed:wght@400;700&display=swap">
<style>
  :root{
    --brand-orange:#f37122;
    --brand-grey:#5c5c5c;
    --white:#ffffff;
    --band-grey:#e6e6e6;
    --band-grey-dark:#cfcfcf;
    --text:#3d3d3d;
  }
  *{box-sizing:border-box;}
  html,body{margin:0;padding:0;width:707px;height:1200px;overflow:hidden;background:var(--white);}
  body{font-family:"Open Sans",Arial,sans-serif;color:var(--text);}

  .chart{position:relative;width:707px;height:1200px;display:flex;flex-direction:column;background:var(--white);}

  /* hero */
  .hero{position:relative;height:470px;flex:none;}
  .hero-visual{
    position:absolute;inset:0;
    background:
      radial-gradient(ellipse at 25% 70%, rgba(255,255,255,.85) 0%, rgba(255,255,255,0) 30%),
      linear-gradient(115deg,#e24a4a 0%,#f2913a 16%,#f6d24a 30%,#8fcf5a 44%,#3fb4a8 56%,#4d8fd6 68%,#8e6fcf 80%,#ec6fa0 92%,#f5a9c0 100%);
  }
  .hero-header{position:absolute;top:0;left:0;width:707px;height:140px;}
  .brand{
    position:absolute;top:26px;left:0;width:707px;
    display:flex;justify-content:center;align-items:center;gap:12px;
  }
  .brand-mark{width:48px;height:48px;border-radius:50%;background:var(--brand-orange);flex:none;}
  .brand-text{display:flex;flex-direction:column;line-height:1;}
  .brand-name{font-weight:700;font-size:34px;color:var(--brand-orange);letter-spacing:-.5px;}
  .brand-tagline{font-size:10.5px;font-weight:600;color:var(--brand-grey);margin-top:4px;}

  /* info */
  .info{text-align:center;padding:14px 44px 0;flex:none;}
  .pill{
    display:inline-block;background:var(--brand-orange);color:var(--white);
    font-family:"Roboto Condensed",Arial,sans-serif;font-size:15px;
    padding:3px 14px;border-radius:6px;box-shadow:0 1px 3px rgba(0,0,0,.3);
  }
  .info p{font-size:12px;line-height:1.45;margin:9px 0 0;}
  .info .recommend{color:var(--brand-orange);}

  /* swatches */
  .swatches{
    display:grid;grid-template-columns:repeat(8,72px);column-gap:13px;row-gap:16px;
    justify-content:center;padding:18px 0 0;flex:none;
  }
  .swatch{text-align:center;}
  .chip{
    width:72px;height:72px;border-radius:4px;
    background-image:linear-gradient(140deg,rgba(255,255,255,.22) 0%,rgba(255,255,255,0) 45%,rgba(0,0,0,.18) 100%);
    box-shadow:0 1px 3px rgba(0,0,0,.3);
  }
  .swatch-name{
    display:block;margin-top:8px;font-family:"Roboto Condensed",Arial,sans-serif;
    font-size:11.5px;color:#2e2e2e;white-space:nowrap;
  }

  /* disclaimer */
  .disclaimer{
    margin-top:auto;background:linear-gradient(#f1f1f1,#e9e9e9);
    text-align:center;padding:10px 60px 12px;
  }
  .disclaimer h2{
    margin:0;font-family:"Roboto Condensed",Arial,sans-serif;font-weight:700;
    font-size:17px;color:var(--brand-orange);
  }
  .disclaimer p{margin:6px 0 0;font-size:10px;line-height:1.45;color:#444;}

  /* footer */
  .footer{
    height:44px;background:var(--brand-orange);color:var(--white);
    display:flex;align-items:center;justify-content:space-between;padding:0 22px;flex:none;
  }
  .footer-web{font-size:9.5px;display:flex;align-items:center;gap:5px;}
  .footer-web strong{font-size:12px;font-weight:600;}
  .footer-phone{display:flex;align-items:center;gap:9px;font-family:"Roboto Condensed",Arial,sans-serif;font-weight:700;font-size:25px;}
</style>
</head>
<body>
<main class="chart">

  <section class="hero">
    <div class="hero-visual" role="img" aria-label="Fanned-out rainbow paint colour swatch cards with a blue paintbrush resting on top"></div>
    <svg class="hero-header" viewBox="0 0 707 140" aria-hidden="true">
      <defs>
        <linearGradient id="headerShade" x1="0" y1="0" x2="0" y2="1">
          <stop offset="0" stop-color="#f4f4f4"/>
          <stop offset="1" stop-color="#d9d9d9"/>
        </linearGradient>
      </defs>
      <polygon points="0,0 707,0 707,18 354,118 0,18" fill="url(#headerShade)"/>
      <polyline points="0,18 354,118 707,18" fill="none" stroke="#ffffff" stroke-width="4"/>
    </svg>
    <div class="brand">
      <span class="brand-mark"></span>
      <span class="brand-text">
        <span class="brand-name">Resinex Pro</span>
        <span class="brand-tagline">Resin coatings and a whole lot more.</span>
      </span>
    </div>
  </section>

  <section class="info">
    <span class="pill">Additional Info To Add</span>
    <p>Resinex Pro Shimmer Tint Powders are special effect pigments composed of mica nano-particles coated with various organic and inorganic pigments to create pearlescent and iridescent effects that mimic the natural look of stone and rock formations.</p>
    <p>These unique pigments are designed to be field blended with Resinex Pro Artisan Lustre clear epoxy. When the metallic particles are mixed with our epoxy they give the coating a shine that reflects light and creates an eye-catching dramatic color</p>
    <p class="recommend">For the most vivid color and dynamic effects we recommend<br>(1) 16oz jar of metallic pigment for each 3 Gallon kit of our Artisan Lustre Epoxy.</p>
  </section>

  <section class="swatches">
    <div class="swatch"><div class="chip" style="background-color:#b3103f"></div><span class="swatch-name">BUBBLEGUM</span></div>
    <div class="swatch"><div class="chip" style="background-color:#f0560c"></div><span class="swatch-name">TANGERINE</span></div>
    <div class="swatch"><div class="chip" style="background-color:#d0780e"></div><span class="swatch-name">ORANGE GOLD</span></div>
    <div class="swatch"><div class="chip" style="background-color:#a4370b"></div><span class="swatch-name">COPPER</span></div>
    <div class="swatch"><div class="chip" style="background-color:#8a2c14"></div><span class="swatch-name">CINNAMON</span></div>
    <div class="swatch"><div class="chip" style="background-color:#7a1012"></div><span class="swatch-name">WINE RED</span></div>
    <div class="swatch"><div class="chip" style="background-color:#6c3114"></div><span class="swatch-name">PENNY</span></div>
    <div class="swatch"><div class="chip" style="background-color:#b5560c"></div><span class="swatch-name">BRASS</span></div>

    <div class="swatch"><div class="chip" style="background-color:#f2b503"></div><span class="swatch-name">CANARY</span></div>
    <div class="swatch"><div class="chip" style="background-color:#d98f12"></div><span class="swatch-name">CAIRO</span></div>
    <div class="swatch"><div class="chip" style="background-color:#998912"></div><span class="swatch-name">OLIVE YELLOW</span></div>
    <div class="swatch"><div class="chip" style="background-color:#109b7f"></div><span class="swatch-name">SEA GREEN</span></div>
    <div class="swatch"><div class="chip" style="background-color:#1d4f39"></div><span class="swatch-name">FOREST GREEN</span></div>
    <div class="swatch"><div class="chip" style="background-color:#2a4a2d"></div><span class="swatch-name">GREEN APPLE</span></div>
    <div class="swatch"><div class="chip" style="background-color:#3a2011"></div><span class="swatch-name">COFFEE</span></div>
    <div class="swatch"><div class="chip" style="background-color:#151515"></div><span class="swatch-name">GUNMETAL</span></div>

    <div class="swatch"><div class="chip" style="background-color:#ecddd5"></div><span class="swatch-name">PEARL</span></div>
    <div class="swatch"><div class="chip" style="background-color:#c3c3c5"></div><span class="swatch-name">DIAMOND</span></div>
    <div class="swatch"><div class="chip" style="background-color:#78716f"></div><span class="swatch-name">SILVER</span></div>
    <div class="swatch"><div class="chip" style="background-color:#4e4a4a"></div><span class="swatch-name">TITANIUM</span></div>
    <div class="swatch"><div class="chip" style="background-color:#13779b"></div><span class="swatch-name">SKY BLUE</span></div>
    <div class="swatch"><div class="chip" style="background-color:#1550a8"></div><span class="swatch-name">OCEAN BLUE</span></div>
    <div class="swatch"><div class="chip" style="background-color:#7344a6"></div><span class="swatch-name">LILAC</span></div>
    <div class="swatch"><div class="chip" style="background-color:#2f106f"></div><span class="swatch-name">GRAPE</span></div>
  </section>

  <section class="disclaimer">
    <h2>Disclaimer</h2>
    <p>The colors on this chart are represented as closely as possible. Variations should be expected due to differences in substrate conditions, thickness of application, speed of curing, blending of colors, application technique, color of initial primer coat and screen resolution.</p>
  </section>

  <footer class="footer">
    <span class="footer-web">For additional information and application instructions visit-
      <svg width="12" height="12" viewBox="0 0 12 12" aria-hidden="true"><circle cx="6" cy="6" r="5.2" fill="none" stroke="#fff" stroke-width="1.2"/><ellipse cx="6" cy="6" rx="2.2" ry="5.2" fill="none" stroke="#fff" stroke-width="1"/><line x1="0.8" y1="6" x2="11.2" y2="6" stroke="#fff" stroke-width="1"/></svg>
      <strong>www.resinexpro-sample.com</strong></span>
    <span class="footer-phone">
      <svg width="24" height="24" viewBox="0 0 24 24" aria-hidden="true"><path d="M6.6 2.5l3 3.6-1.9 2.3c1.2 2.6 3.3 4.7 5.9 5.9l2.3-1.9 3.6 3-1.7 3.4c-.3.6-1 .9-1.7.7C9.8 17.8 6.2 14.2 4.5 7.9c-.2-.7.1-1.4.7-1.7z" fill="none" stroke="#fff" stroke-width="1.8" stroke-linejoin="round"/><path d="M14 3.5a7 7 0 0 1 6.5 6.5M14 7a3.5 3.5 0 0 1 3 3" fill="none" stroke="#fff" stroke-width="1.6" stroke-linecap="round"/></svg>
      1-800-555-0147
    </span>
  </footer>

</main>
</body>
</html>
```